Homepage for a Workout + Food Tracking Mobile App

We need a design for the homepage of our workout and food tracking app called FitBrook (working name, most likely not finalized). The app has many uses, namely a "Strength Review", food logging, workout tracking, statistics/analytics, an AI powered form review tool and an ability to ask an AI any workout, nutrition or app related questions. The homepage should feature some way to access the above listed features as well as an outline, 3d design, diagram or any other way to represent the human body split up into muscle groups for the user to see what muscles they've hit in any amount of time. There should be a section for a profile picture, username, "trophy case" with room for ideally 3 small "trophy" icons.
The main colour should be gold/dark yellow (I used #DEA30A) but I am very flexible on that and I'm curious to try out other colours. The background colour I am also flexible on, I went with a dark gray.
The screenshot I uploaded is in no way what your design needs to look like. Use it more to check what buttons and elements should be present.
I'll likely need more designs for other screens in the future and will be happy to work further with the designer chosen.
Target Market(s)
Gymgoers, People on a diet, Weightlifters,
Look and feel

```html
<!DOCTYPE html>
<html lang="en">
<head>
<meta charset="UTF-8">
<title>FitBrook – Home</title>
<link href="https://fonts.googleapis.com/css2?family=Barlow:wght@500;600;700&display=swap" rel="stylesheet">
<style>
  :root {
    --gold: #ebbd6c;
    --gold-deep: #dca22f;
    --blue: #74bedb;
    --terracotta: #d87d57;
    --peach-bg: #fdf0e0;
    --blue-bg: #e8f1f5;
    --rose-bg: #f9ece7;
    --panel-bg: #fdf3e4;
    --ink: #2b2b2b;
    --muted: #444;
    --icon: #9a9a9a;
    --white: #ffffff;
  }
  * { box-sizing: border-box; margin: 0; padding: 0; }
  html, body { width: 684px; height: 1200px; overflow: hidden; }
  body {
    background: var(--white);
    font-family: "Barlow", Arial, sans-serif;
    color: var(--ink);
    position: relative;
  }
  .profile { position: absolute; left: 42px; top: 36px; width: 160px; text-align: center; }
  .avatar {
    width: 156px; height: 156px; border-radius: 50%;
    border: 3px solid var(--gold);
    padding: 6px; background: var(--white);
  }
  .avatar-photo {
    width: 100%; height: 100%; border-radius: 50%;
    background: radial-gradient(circle at 50% 40%, #8a7f74, #4a443f 60%, #2e2b29);
  }
  .username { margin-top: 10px; font-size: 23px; font-weight: 500; }
  .trophy-case {
    position: absolute; left: 290px; top: 40px; width: 342px; height: 128px;
    background: var(--white);
    box-shadow: 0 6px 22px rgba(0,0,0,0.08);
    display: flex; align-items: center; justify-content: center; gap: 22px;
  }
  .stats {
    position: absolute; left: 40px; right: 40px; top: 252px;
    display: grid; grid-template-columns: repeat(4, 1fr); gap: 16px;
  }
  .stat { height: 128px; border-radius: 14px; text-align: center; padding-top: 22px; }
  .stat-value { font-size: 44px; font-weight: 700; line-height: 1; }
  .stat-label { margin-top: 14px; font-size: 19px; font-weight: 500; color: var(--muted); }
  .stat--followers { background: var(--peach-bg); }
  .stat--followers .stat-value { color: var(--gold); }
  .stat--trophies { background: var(--blue-bg); }
  .stat--trophies .stat-value { color: var(--blue); }
  .stat--medals { background: var(--rose-bg); }
  .stat--medals .stat-value { color: #d99a6c; }
  .stat--workouts { background: var(--peach-bg); }
  .stat--workouts .stat-value { color: #dca24a; }
  .muscle-map {
    position: absolute; left: 80px; right: 80px; top: 410px; height: 300px;
    background: radial-gradient(ellipse at 50% 50%, #e7b59c 0%, #f4ddd0 45%, #ffffff 75%);
  }
  .actions {
    position: absolute; left: 40px; right: 40px; top: 730px; height: 340px;
    background: var(--panel-bg); border-radius: 12px;
    padding: 30px 30px;
    display: grid; grid-template-columns: 1fr 1fr; gap: 24px 36px;
  }
  .action {
    height: 56px; border-radius: 28px; border: none;
    color: var(--white); font-family: inherit; font-size: 18px; font-weight: 700;
    box-shadow: 0 4px 10px rgba(0,0,0,0.12);
    display: flex; align-items: center; justify-content: center;
  }
  .action--gold { background: var(--gold); }
  .action--blue { background: var(--blue); }
  .action--wide { grid-column: 1 / -1; background: var(--terracotta); }
  .tab-bar {
    position: absolute; left: 0; right: 0; bottom: 0; height: 110px;
    display: flex; justify-content: space-around; align-items: center; padding: 0 40px;
  }
  .tab-bar svg { width: 40px; height: 40px; fill: none; stroke-width: 2.2; stroke-linecap: round; stroke-linejoin: round; }
  .tab-bar .tab { stroke: var(--icon); }
  .tab-bar .tab--active { stroke: var(--gold-deep); }
</style>
</head>
<body>
  <section class="profile">
    <div class="avatar"><div class="avatar-photo" role="img" aria-label="User profile photo"></div></div>
    <p class="username">@username</p>
  </section>

  <section class="trophy-case" aria-label="Trophy case">
    <svg width="68" height="84" viewBox="0 0 60 74" aria-hidden="true">
      <path d="M14 6h32v18a16 16 0 0 1-32 0z" fill="#f2b51d"/>
      <path d="M14 12H5a9 9 0 0 0 11 14M46 12h9a9 9 0 0 1-11 14" stroke="#f2b51d" stroke-width="4" fill="none"/>
      <rect x="26" y="40" width="8" height="14" fill="#e5a412"/>
      <rect x="16" y="54" width="28" height="8" fill="#f2b51d"/>
      <rect x="12" y="62" width="36" height="6" fill="#c9693d"/>
      <path d="M30 12l3 6 6 1-4.5 4 1 6-5.5-3-5.5 3 1-6-4.5-4 6-1z" fill="#fff"/>
    </svg>
    <svg width="80" height="98" viewBox="0 0 60 74" aria-hidden="true">
      <path d="M14 6h32v18a16 16 0 0 1-32 0z" fill="#f2b51d"/>
      <path d="M14 12H5a9 9 0 0 0 11 14M46 12h9a9 9 0 0 1-11 14" stroke="#f2b51d" stroke-width="4" fill="none"/>
      <rect x="26" y="40" width="8" height="14" fill="#e5a412"/>
      <rect x="16" y="54" width="28" height="8" fill="#f2b51d"/>
      <rect x="12" y="62" width="36" height="6" fill="#c9693d"/>
      <path d="M30 12l3 6 6 1-4.5 4 1 6-5.5-3-5.5 3 1-6-4.5-4 6-1z" fill="#fff"/>
    </svg>
    <svg width="64" height="78" viewBox="0 0 60 74" aria-hidden="true">
      <path d="M14 6h32v18a16 16 0 0 1-32 0z" fill="#f2b51d"/>
      <path d="M14 12H5a9 9 0 0 0 11 14M46 12h9a9 9 0 0 1-11 14" stroke="#f2b51d" stroke-width="4" fill="none"/>
      <rect x="26" y="40" width="8" height="14" fill="#e5a412"/>
      <rect x="16" y="54" width="28" height="8" fill="#f2b51d"/>
      <rect x="12" y="62" width="36" height="6" fill="#c9693d"/>
      <path d="M30 12l3 6 6 1-4.5 4 1 6-5.5-3-5.5 3 1-6-4.5-4 6-1z" fill="#fff"/>
    </svg>
  </section>

  <section class="stats">
    <div class="stat stat--followers"><div class="stat-value">38</div><div class="stat-label">Followers</div></div>
    <div class="stat stat--trophies"><div class="stat-value">4</div><div class="stat-label">Trophies</div></div>
    <div class="stat stat--medals"><div class="stat-value">1</div><div class="stat-label">Medals</div></div>
    <div class="stat stat--workouts"><div class="stat-value">107</div><div class="stat-label">Workouts</div></div>
  </section>

  <div class="muscle-map" role="img" aria-label="Anatomical muscle map of the human body shown from front, back and side"></div>

  <nav class="actions">
    <button class="action action--gold">Strength Review</button>
    <button class="action action--blue">Log Food</button>
    <button class="action action--blue">Start Workout</button>
    <button class="action action--gold">View Statictics</button>
    <button class="action action--wide">AI From Review Tool</button>
    <button class="action action--wide">Ask FitBrook AI</button>
  </nav>

  <footer class="tab-bar">
    <svg class="tab--active" viewBox="0 0 24 24" aria-label="Home"><path d="M4 10.5 12 4l8 6.5V20h-5v-6h-6v6H4z"/></svg>
    <svg class="tab" viewBox="0 0 24 24" aria-label="Log"><rect x="5" y="5" width="14" height="16" rx="2"/><rect x="9" y="3" width="6" height="4" rx="1"/><path d="M9 11h6M9 15h6"/></svg>
    <svg class="tab" viewBox="0 0 24 24" aria-label="Statistics"><path d="M11 5a8 8 0 1 0 8 8h-8z"/><path d="M14 3a7 7 0 0 1 7 7h-7z"/></svg>
    <svg class="tab" viewBox="0 0 24 24" aria-label="Profile"><circle cx="12" cy="8" r="4"/><path d="M4 21c0-4.5 3.6-7 8-7s8 2.5 8 7z"/></svg>
  </footer>
</body>
</html>
```